Author and Publisher

Cover for a book on the process of publishing a book from the presentation to the publisher until the selling in bookstores :
A behind-the-scenes journey through the world of book publishing, from manuscript to bookstore. The book explores the relationship between authors and publishers, manuscript selection, contracts, editing, proofreading, book design, printing, distribution, bookstores and online sales. It reveals the many people, decisions and processes involved in turning a text into a physical book and bringing it to readers. The illustration should evoke publishing as a lively, contemporary ecosystem, combining creativity, craftsmanship, business and the enduring appeal of books.
FORMAT : 14 x 20,5 cm
AUTHOR : Luc Varennes
TITLE : Le scribe et la presse
PUBLISHER : Editions Trovel (at the bottom of the page)
Target Market(s)
General public, mainly news authors of books
Look and feel
Each slider illustrates characteristics of the customer's brand and the style your logo design should communicate.

```html
<!DOCTYPE html>
<html lang="fr">
<head>
<meta charset="utf-8">
<title>Le scribe et la presse — Luc Varennes</title>
<link rel="stylesheet" href="https://fonts.googleapis.com/css2?family=Bodoni+Moda:opsz,wght@6..96,400;6..96,600&family=Libre+Caslon+Text:wght@400&display=swap">
<style>
  :root {
    --page-bg: #f4f4f4;
    --ink: #111010;
    --ink-soft: #2a2622;
    --parchment-light: #f1ece9;
    --parchment-mid: #e6cfa6;
    --parchment-gold: #d19a3f;
    --parchment-deep: #b97a25;
    --engraving-light: #ece4dc;
    --engraving-mid: #b7a79a;
    --engraving-dark: #5a4a3e;
  }
  * { margin: 0; padding: 0; box-sizing: border-box; }
  html, body {
    width: 1200px;
    height: 1099px;
    overflow: hidden;
    background: var(--page-bg);
  }
  .book-cover {
    position: absolute;
    left: 258px;
    top: 50px;
    width: 683px;
    height: 1000px;
    background:
      radial-gradient(ellipse 62% 58% at 50% 45%, var(--parchment-light) 0%, var(--parchment-light) 35%, var(--parchment-mid) 62%, var(--parchment-gold) 85%, var(--parchment-deep) 100%);
    color: var(--ink);
    text-align: center;
  }
  .cover-title {
    position: absolute;
    top: 78px;
    left: 0;
    width: 100%;
    font-family: "Bodoni Moda", "Didot", serif;
    font-weight: 400;
    font-size: 122px;
    line-height: 124px;
    letter-spacing: -2px;
    transform: scaleX(0.86);
  }
  .cover-divider {
    position: absolute;
    top: 352px;
    left: 218px;
    width: 247px;
    height: 26px;
  }
  .cover-author {
    position: absolute;
    top: 392px;
    left: 0;
    width: 100%;
    font-family: "Libre Caslon Text", "Times New Roman", serif;
    font-size: 36px;
    color: var(--ink-soft);
    transform: scaleX(0.9);
  }
  .cover-illustration {
    position: absolute;
    top: 500px;
    left: 108px;
    width: 512px;
    height: 310px;
    border-radius: 6px;
    background: radial-gradient(ellipse 60% 55% at 50% 50%, var(--engraving-light) 0%, var(--engraving-mid) 70%, rgba(90,74,62,0.35) 100%);
  }
  .cover-publisher {
    position: absolute;
    top: 925px;
    left: 0;
    width: 100%;
    font-family: "Bodoni Moda", "Didot", serif;
    font-weight: 600;
    font-size: 19px;
    letter-spacing: 0.2em;
    text-transform: uppercase;
    color: var(--ink-soft);
  }
</style>
</head>
<body>
  <main class="book-cover">
    <h1 class="cover-title">Le scribe et<br>la presse</h1>

    <svg class="cover-divider" viewBox="0 0 247 26" aria-hidden="true">
      <line x1="4" y1="13" x2="243" y2="13" stroke="#1a1715" stroke-width="1.4"/>
      <circle cx="4" cy="13" r="2" fill="#1a1715"/>
      <circle cx="243" cy="13" r="2" fill="#1a1715"/>
      <rect x="95" y="5" width="57" height="16" rx="8" fill="#8a7a6a" opacity="0.55" role="img" aria-label="Petit motif décoratif central"/>
    </svg>

    <p class="cover-author">Luc Varennes</p>

    <div class="cover-illustration" role="img" aria-label="Gravure d'un livre ouvert avec une plume d'oie posée en travers des pages"></div>

    <p class="cover-publisher">Editions Trovel</p>
  </main>
</body>
</html>
```